Envelope Design - Winner can do follow-up business

- Marvuno.com is a Swiss-based online store selling business shirts and accessories for business men
- Please visit the webpage to make yourself familiar with the company. Although the text is in German, with Google translator you should be able to understand the main content.
- Our clients are mainly business men between 30 and 60 years old. Mostly with a high income working in the service industry (banking, insurance, lawyers, etc.). Sometimes there wives purchase the shirts for them ;-)
- The colors and the logo are given, as they are also used for the print materials (please see files in attachment)
- I am running several businesses and often need a talented web designer --> the winner gets substantial follow-up business
your task:
-for our company we need a new envelope design
-It should be simple and modern
-please use one of the logos in the followings.
-suprise me :)

```html
<!DOCTYPE html>
<html lang="de">
<head>
<meta charset="utf-8">
<title>Marvuno – Envelope</title>
<link rel="stylesheet" href="https://fonts.googleapis.com/css2?family=Ubuntu:wght@400;500&display=swap">
<style>
  :root {
    --backdrop: #d9d9d9;
    --paper: #ffffff;
    --ink: #2b2a2c;
    --text: #3a3a3a;
    --gold: #e6d466;
    --window-edge: #c9c9c9;
    --haze: #ececec;
  }
  * { box-sizing: border-box; margin: 0; padding: 0; }
  html, body {
    width: 1200px;
    height: 1000px;
    overflow: hidden;
    background: var(--backdrop);
    font-family: "Ubuntu", sans-serif;
  }
  .canvas {
    position: relative;
    width: 1200px;
    height: 1000px;
  }
  .envelope {
    position: absolute;
    left: 60px;
    top: 230px;
    width: 1080px;
    height: 540px;
    background: var(--paper);
    overflow: hidden;
    box-shadow: 0 6px 18px rgba(0,0,0,0.18);
  }
  .envelope__art {
    position: absolute;
    inset: 0;
    width: 100%;
    height: 100%;
  }
  .envelope__texture {
    position: absolute;
    right: 0;
    top: 150px;
    width: 300px;
    height: 220px;
    background: radial-gradient(ellipse at 80% 50%, var(--haze) 0%, rgba(236,236,236,0) 70%);
  }
  .sender {
    position: absolute;
    left: 60px;
    top: 95px;
    color: var(--text);
  }
  .sender__brand {
    display: flex;
    align-items: center;
    gap: 12px;
    font-size: 40px;
    font-weight: 500;
    letter-spacing: 5px;
    color: var(--gold);
    line-height: 1;
  }
  .sender__mark {
    width: 14px;
    height: 14px;
    background: var(--gold);
  }
  .sender__line {
    font-size: 15px;
    font-weight: 400;
    margin-top: 8px;
    letter-spacing: 0.3px;
  }
  .sender__brand + .sender__line { margin-top: 22px; }
  .address-window {
    position: absolute;
    left: 95px;
    top: 215px;
    width: 340px;
    height: 185px;
    border: 1.5px solid var(--window-edge);
    border-radius: 18px;
    background: var(--paper);
  }
</style>
</head>
<body>
<main class="canvas">
  <section class="envelope" aria-label="Marvuno envelope front">
    <div class="envelope__texture" role="img" aria-label="Faint grey geometric pattern"></div>
    <svg class="envelope__art" viewBox="0 0 1080 540" aria-hidden="true">
      <polygon points="0,0 72,0 0,42" fill="var(--gold)"/>
      <path d="M600,430 C820,470 990,410 1080,240 L1080,300 C1000,440 830,480 600,445 Z" fill="var(--gold)"/>
      <path d="M0,360 C180,300 360,345 560,405 C720,452 870,462 1080,432 L1080,540 L0,540 Z" fill="var(--ink)"/>
    </svg>
    <div class="sender">
      <div class="sender__brand"><span class="sender__mark"></span>MARVUNO</div>
      <p class="sender__line">Marvuno GmbH | Lindenweg 7 | 8800-Thalwil</p>
      <p class="sender__line">T.: +41 44 730 48 16 | E.: info@marvuno.com</p>
    </div>
    <div class="address-window"></div>
  </section>
</main>
</body>
</html>
```